Claimant Aid Pathway USA - Email Marketing Creative

Looking for design of email creative for Claimant Aid Pathway USA website. Call to action based email focused on conveying brand, messaging of "Disabled? Unable to Work? You May Qualify for Social Security Disability Benefits", call to action of 'Free Evaluation' or 'Fast, Free, No Obligation Evaluation'. Can use any messaging from the current mock of https://lnkshrt.example/7QwXpR4 . Please focus on imaging of 50+ people if used, red white and blue coloring (patriotic) yet USA looking. Creative must be done in HTML as well as text for easy use and include Email Opt Out link etc. Examples of competitors emails attached. PLEASE DO NOT COPY them. Just use as examples.

Target Market(s)

Disabled American. Age 50+ Looking for help applying, re-applying or handling a social security disability hearing.

Industry/Entity Type

Legal

Font styles to use
Serif
Sans Serif

Colors

Designer to choose colors to be used in the design.

Requirements
Must have
• call to action based html
Nice to have
• strong call to action.
Should not have
• Should not be cookie cutter. Stick to simple yet official looking.

```html
<!DOCTYPE html>
<html lang="en">
<head>
<meta charset="utf-8">
<title>Claimant Aid Pathway USA - Free Evaluation</title>
<link rel="stylesheet" href="https://fonts.googleapis.com/css2?family=Roboto:wght@300;400;500;700&family=Roboto+Condensed:wght@700&display=swap">
<style>
  :root{
    --navy:#0f1a3a;
    --red:#e4002b;
    --red-dark:#c4001f;
    --text:#555a60;
    --ink:#1c1c1c;
    --hero-grey:#e2e3e6;
    --panel:#f7f7f7;
    --rule:#dedede;
    --white:#ffffff;
  }
  *{box-sizing:border-box;margin:0;padding:0}
  html,body{width:1200px;height:2980px;overflow:hidden;background:var(--white)}
  body{font-family:"Roboto",Arial,sans-serif;color:var(--text);position:relative}
  .topline{position:absolute;left:0;top:0;width:1200px;height:7px;background:var(--red)}

  .brand{position:absolute;left:90px;top:38px;display:flex;align-items:center;gap:18px}
  .brand-dot{width:130px;height:130px;border-radius:50%;background:var(--navy)}
  .brand-name{font-family:"Roboto",Arial,sans-serif;font-weight:700;font-size:34px;line-height:1.15;color:var(--navy);width:260px}

  .btn-eval{position:absolute;left:727px;top:66px;width:381px;height:77px;border-radius:40px;background:var(--navy);color:var(--white);font-size:33px;font-weight:500;display:flex;align-items:center;justify-content:center;text-decoration:none}

  .hero{position:absolute;left:0;top:200px;width:1200px;height:635px;background:var(--hero-grey);overflow:hidden}
  .hero-photo{position:absolute;left:520px;top:0;width:680px;height:635px;background:linear-gradient(90deg,rgba(226,227,230,1) 0%,#c9c4bd 25%,#b8b0a6 55%,#8e97b0 80%,#d8d6d2 100%)}
  .hero-title{position:absolute;left:90px;top:125px;font-family:"Roboto Condensed","Arial Narrow",sans-serif;font-weight:700;font-size:62px;line-height:80px;color:var(--navy)}
  .hero-title .accent{color:var(--red);display:block}
  .hero-sub{position:absolute;left:90px;top:300px;font-size:38px;line-height:50px;color:var(--ink);font-weight:400}
  .hero-banner{position:absolute;left:90px;top:440px;width:925px;height:57px;background:var(--red);clip-path:polygon(20px 0,100% 0,100% 100%,0 100%);color:var(--white);font-size:29px;font-weight:500;display:flex;align-items:center;padding-left:47px}

  .seal{position:absolute;left:541px;width:118px;height:118px;border-radius:50%;background:var(--white);box-shadow:0 2px 8px rgba(0,0,0,.12);display:flex;align-items:center;justify-content:center}
  .seal span{width:72px;height:72px;border-radius:50%;background:var(--navy)}
  .seal-hero{top:776px}
  .seal-foot{top:2764px}

  .copy{position:absolute;left:113px;width:975px;font-size:28px;line-height:59px;font-weight:300;color:var(--text)}
  .copy-intro{top:920px;text-align:center;left:110px;width:980px}
  .copy-a{top:1465px;text-align:justify;text-align-last:center}
  .copy-b{top:1790px;text-align:justify;text-align-last:center}

  .features{position:absolute;left:95px;top:1141px;width:1012px;height:269px;background:var(--panel);border:1px solid var(--rule);padding:30px 0 0 30px;display:grid;grid-template-columns:535px 440px}
  .features ul{list-style:none}
  .features li{display:flex;align-items:flex-start;gap:32px;font-size:30px;font-weight:500;color:var(--ink);line-height:55px}
  .features svg{flex:none;margin-top:13px}

  .btn-apply{position:absolute;left:447px;top:2200px;width:308px;height:76px;border-radius:40px;background:linear-gradient(180deg,#f21434,var(--red-dark));color:var(--white);font-size:33px;font-weight:500;display:flex;align-items:center;justify-content:center;gap:20px;text-decoration:none}

  .rule{position:absolute;left:90px;top:2367px;width:1018px;height:2px;background:var(--rule)}
  .notice{position:absolute;left:90px;top:2425px;width:1018px;text-align:center;font-size:34px;line-height:54px;color:var(--ink);font-weight:400}
  .notice a{color:var(--red);text-decoration:underline}
  .contact{position:absolute;left:0;top:2560px;width:1200px;display:flex;justify-content:center;align-items:center;gap:14px;font-size:27px;font-weight:300;color:var(--text)}
  .contact .sep{margin:0 10px}
  .social{position:absolute;left:0;top:2660px;width:1200px;display:flex;justify-content:center;gap:14px}
  .social a{width:65px;height:65px;border-radius:50%;background:var(--navy);display:block}

  .footer{position:absolute;left:0;top:2853px;width:1200px;height:127px;background:var(--navy);color:var(--white);font-size:24px;display:flex;align-items:center;justify-content:center;padding-top:22px}
</style>
</head>
<body>
  <div class="topline"></div>

  <header>
    <div class="brand"><span class="brand-dot"></span><span class="brand-name">Claimant Aid Pathway USA</span></div>
    <a class="btn-eval" href="https://lnkshrt.example/7QwXpR4">FREE EVALUATION</a>
  </header>

  <section class="hero">
    <div class="hero-photo" role="img" aria-label="Photo of an older couple at home reviewing paperwork at a laptop"></div>
    <h1 class="hero-title">UNABLE TO WORK<span class="accent">DUE TO DISABILITY?</span></h1>
    <p class="hero-sub">We help Americans get the<br>benefits they deserve!</p>
    <div class="hero-banner">YOU MAY QUALITY FOR BENEFITS OF UP TO $2,642.00/MONTH!</div>
  </section>
  <div class="seal seal-hero"><span></span></div>

  <p class="copy copy-intro">Sed ut perspiciatis unde omnis iste natus error sit voluptatem accusantium<br>doloremque laudantium, totam rem aperiam, eaque ipsa quae ab illo inven-<br>tore veritatis et quasi architecto beatae vitae dicta sunt explicabo.</p>

  <section class="features">
    <ul>
      <li><svg width="28" height="28" viewBox="0 0 28 28"><circle cx="14" cy="14" r="14" fill="#e4002b"/><path d="M8 14.5l4 4 8-8.5" stroke="#fff" stroke-width="3.2" fill="none" stroke-linecap="round" stroke-linejoin="round"/></svg>We deal with the government</li>
      <li><svg width="28" height="28" viewBox="0 0 28 28"><circle cx="14" cy="14" r="14" fill="#e4002b"/><path d="M8 14.5l4 4 8-8.5" stroke="#fff" stroke-width="3.2" fill="none" stroke-linecap="round" stroke-linejoin="round"/></svg>100% Free Evaluation Service!</li>
      <li><svg width="28" height="28" viewBox="0 0 28 28"><circle cx="14" cy="14" r="14" fill="#e4002b"/><path d="M8 14.5l4 4 8-8.5" stroke="#fff" stroke-width="3.2" fill="none" stroke-linecap="round" stroke-linejoin="round"/></svg>Get the benefits you deserve!</li>
    </ul>
    <ul>
      <li><svg width="28" height="28" viewBox="0 0 28 28"><circle cx="14" cy="14" r="14" fill="#e4002b"/><path d="M8 14.5l4 4 8-8.5" stroke="#fff" stroke-width="3.2" fill="none" stroke-linecap="round" stroke-linejoin="round"/></svg>Fast,Easy and secure!</li>
      <li><svg width="28" height="28" viewBox="0 0 28 28"><circle cx="14" cy="14" r="14" fill="#e4002b"/><path d="M8 14.5l4 4 8-8.5" stroke="#fff" stroke-width="3.2" fill="none" stroke-linecap="round" stroke-linejoin="round"/></svg>Takes less tha 2 minutes!</li>
      <li><svg width="28" height="28" viewBox="0 0 28 28"><circle cx="14" cy="14" r="14" fill="#e4002b"/><path d="M8 14.5l4 4 8-8.5" stroke="#fff" stroke-width="3.2" fill="none" stroke-linecap="round" stroke-linejoin="round"/></svg><span>Previous denials &amp; new applicants!</span></li>
    </ul>
  </section>

  <p class="copy copy-a">Nemo enim ipsam voluptatem quia voluptas sit aspernatur aut odit aut fugit, sed quia consequuntur magni dolores eos qui ratione voluptatem sequi nesciunt. Neque porro quisquam est, qui dolorem ipsum quia dolor sit amet, consectetur, adipisci velit, sed quia non numquam eius modi tempora incidunt ut labore et dolore magnam aliquam quaerat voluptatem.</p>

  <p class="copy copy-b">But I must explain to you how all this mistaken idea of denouncing pleasure and praising pain was born and I will give you a complete account of the system, and expound the actual teachings of the great explorer of the truth, the mas-ter&#8209;builder of humBut I must explain to you how all this mistaken idea of denouncing pleasure and praising pain was born and I will give you a complete account of the system, and expound the actual teachings</p>

  <a class="btn-apply" href="https://lnkshrt.example/7QwXpR4">APPLY NOW
    <svg width="46" height="46" viewBox="0 0 46 46"><circle cx="23" cy="23" r="21" fill="#fff"/><circle cx="23" cy="23" r="14" fill="none" stroke="#e4002b" stroke-width="3.5"/><path d="M16 23h13M23.5 17l6 6-6 6" stroke="#e4002b" stroke-width="3.5" fill="none" stroke-linecap="round" stroke-linejoin="round"/></svg>
  </a>

  <div class="rule"></div>

  <p class="notice">You need tis newsletter because you have subscribed to exclusive onlinepromo Newsletter to subscribe,please <a href="https://lnkshrt.example/7QwXpR4">Visit here</a></p>

  <div class="contact">
    <svg width="18" height="24" viewBox="0 0 18 24"><path d="M9 0C4 0 0 4 0 9c0 6.5 9 15 9 15s9-8.5 9-15c0-5-4-9-9-9zm0 12.5A3.5 3.5 0 1 1 9 5.5a3.5 3.5 0 0 1 0 7z" fill="#e4002b"/></svg>
    <span>418,Liberty Plaza Suite 12</span><span class="sep">|</span>
    <svg width="22" height="22" viewBox="0 0 24 24"><path d="M6.6 10.8a15 15 0 0 0 6.6 6.6l2.2-2.2c.3-.3.7-.4 1-.2 1.1.4 2.3.6 3.6.6.6 0 1 .4 1 1V20c0 .6-.4 1-1 1A17 17 0 0 1 3 4c0-.6.4-1 1-1h3.5c.6 0 1 .4 1 1 0 1.3.2 2.5.6 3.6.1.3 0 .7-.2 1z" fill="#e4002b"/></svg>
    <span>1 800 555 0142</span>
  </div>

  <nav class="social" aria-label="Social channels">
    <a href="#" aria-label="Social channel 1"></a>
    <a href="#" aria-label="Social channel 2"></a>
    <a href="#" aria-label="Social channel 3"></a>
    <a href="#" aria-label="Social channel 4"></a>
    <a href="#" aria-label="Social channel 5"></a>
  </nav>

  <footer class="footer">Copyrights © 2019, Claimant Aid Pathway USA . All Rights Reserved.</footer>
  <div class="seal seal-foot"><span></span></div>
</body>
</html>
```